Business Card Design

Online clothing womens clothing store, I sell my clothing online and at the markets.

i would like the attached picture on the front of the card and the contact information on the back.

Industry/Entity Type

Business

Contact Information for Business Card

Velvet Harbour
Marnie Talbot
(Instagram symbol) _velvet_harbour_
(Facebook symbol) www.facepage-example.com/velvetharbourau/

W : www.velvetharbour-example.com.au
E : info@velvetharbour-example.com.au
P : 0491876324

```html
<!DOCTYPE html>
<html lang="en">
<head>
<meta charset="utf-8">
<title>Velvet Harbour — Business Card</title>
<link rel="stylesheet" href="https://fonts.googleapis.com/css2?family=Open+Sans:wght@400;600;700&display=swap">
<style>
  :root {
    --page-bg: #e9e6e1;
    --card-white: #ffffff;
    --card-black: #1e1e1e;
    --ink-dark: #1a1a1a;
    --ink-light: #f2f2f2;
    --wash-light: #e4e8ea;
    --wash-mid: #b9c3c8;
    --wash-deep: #5f6f78;
  }
  * { box-sizing: border-box; margin: 0; padding: 0; }
  html, body { width: 1200px; height: 900px; overflow: hidden; }
  body {
    background: var(--page-bg);
    font-family: "Open Sans", Arial, sans-serif;
    display: flex;
    flex-direction: column;
    align-items: center;
    justify-content: center;
    gap: 40px;
  }
  .card {
    width: 680px;
    height: 388px;
    position: relative;
    overflow: hidden;
    box-shadow: 0 6px 18px rgba(0,0,0,0.18);
  }

  /* Front */
  .card-front { background: var(--card-black); }
  .front-artwork {
    position: absolute;
    inset: 0 0 38% 0;
    background:
      radial-gradient(ellipse 55% 90% at 78% 40%, var(--wash-deep) 0%, var(--wash-mid) 55%, transparent 80%),
      linear-gradient(100deg, var(--wash-light) 0%, #d6dcdf 55%, var(--wash-mid) 100%);
  }
  .front-band {
    position: absolute;
    inset: 62% 0 0 0;
    background: var(--card-black);
    display: flex;
    align-items: center;
    justify-content: center;
  }
  .brand-name {
    color: var(--ink-light);
    font-weight: 700;
    font-size: 52px;
    letter-spacing: 3px;
    text-transform: uppercase;
  }

  /* Back */
  .card-back { background: var(--card-white); }
  .back-name-area {
    position: absolute;
    inset: 0 0 55% 0;
    display: flex;
    align-items: center;
    justify-content: center;
  }
  .person-name {
    color: var(--ink-dark);
    font-weight: 600;
    font-size: 27px;
    letter-spacing: 0.5px;
    text-transform: uppercase;
    margin-top: 40px;
  }
  .back-band {
    position: absolute;
    inset: 45% 0 0 0;
    background: var(--card-black);
    color: var(--ink-light);
    font-size: 15px;
  }
  .contact-right {
    position: absolute;
    top: 22px;
    right: 32px;
    display: flex;
    flex-direction: column;
    align-items: flex-end;
    gap: 10px;
  }
  .contact-left {
    position: absolute;
    top: 60px;
    left: 44px;
    display: flex;
    flex-direction: column;
    gap: 8px;
  }
  .contact-line { display: flex; align-items: center; gap: 10px; white-space: nowrap; }
  .icon { width: 14px; height: 14px; flex: none; }
  .social-url {
    position: absolute;
    bottom: 40px;
    left: 0; right: 0;
    text-align: center;
  }
</style>
</head>
<body>

  <section class="card card-front" aria-label="Card front">
    <div class="front-artwork" role="img" aria-label="Soft grey and teal watercolour artwork"></div>
    <div class="front-band">
      <span class="brand-name">Velvet Harbour</span>
    </div>
  </section>

  <section class="card card-back" aria-label="Card back">
    <div class="back-name-area">
      <h1 class="person-name">Marnie Talbot</h1>
    </div>
    <div class="back-band">
      <div class="contact-right">
        <div class="contact-line">
          <span>0491876324</span>
          <svg class="icon" viewBox="0 0 24 24" aria-hidden="true"><path fill="currentColor" d="M6.6 10.8a15.1 15.1 0 0 0 6.6 6.6l2.2-2.2c.3-.3.7-.4 1-.2 1.1.4 2.3.6 3.6.6.6 0 1 .4 1 1V20c0 .6-.4 1-1 1A17 17 0 0 1 3 4c0-.6.4-1 1-1h3.5c.6 0 1 .4 1 1 0 1.3.2 2.5.6 3.6.1.3 0 .7-.2 1z"/></svg>
        </div>
        <div class="contact-line">
          <span>info@velvetharbour-example.com.au</span>
          <svg class="icon" viewBox="0 0 24 24" aria-hidden="true"><rect x="2" y="5" width="20" height="14" fill="currentColor"/><path d="M2 5l10 8 10-8" fill="none" stroke="#1e1e1e" stroke-width="2"/></svg>
        </div>
      </div>
      <div class="contact-left">
        <div class="contact-line">
          <svg class="icon" viewBox="0 0 24 24" aria-hidden="true"><path d="M10 14a4 4 0 0 0 5.7 0l3.5-3.5a4 4 0 0 0-5.7-5.7L12 6.3M14 10a4 4 0 0 0-5.7 0l-3.5 3.5a4 4 0 0 0 5.7 5.7l1.5-1.5" fill="none" stroke="currentColor" stroke-width="2" stroke-linecap="round"/></svg>
          <span>www.velvetharbour-example.com.au</span>
        </div>
        <div class="contact-line">
          <svg class="icon" viewBox="0 0 24 24" aria-hidden="true"><rect x="3" y="3" width="18" height="18" fill="currentColor"/></svg>
          <span>_velvet_harbour_</span>
        </div>
      </div>
      <p class="social-url">www.facepage-example.com/velvetharbourau/</p>
    </div>
  </section>

</body>
</html>
```